Digital Product Store Front for Educational Leaders (PraisewithPellar)

I am an a Principal, Author and Education consultant I am in need of a wordpress website that fits my brand that I will be able to sell digital products I have created, digital courses I have created, and offer mentorship and coaching services. I have my branding documents and my content/wording in the files. This website should be professional yet relatable. I'd like it to be clean, easy to navigate and be very obvious with its purpose. Please view the attached documents to give a much clearer idea about my brand and wants. :)

Target Market(s)

Educational Leaders (Principals)

Industry/Entity Type

Educational Leadership

Coding

Coded - Design and coding required

Number of Pages Required

1 page

Font styles to use
Other font styles liked:
• please use my branding font

Requirements
Must have
• All the items I listed on my document, my brand colors and font, The content I submitted is still in a very draft format but just to give the designer and idea.

```html
<!DOCTYPE html>
<html lang="en">
<head>
<meta charset="utf-8">
<title>PraisewithPellar</title>
<link href="https://fonts.googleapis.com/css2?family=Jost:wght@300;400&family=Poppins:wght@300;400;500&display=swap" rel="stylesheet">
<style>
:root{
  --teal:#5b9d93;
  --teal-dark:#4f9187;
  --teal-light:#a6ccc5;
  --cream:#f5efe5;
  --white:#ffffff;
  --ink:#2d2d2d;
  --muted:#555555;
  --pale:#e3eeeb;
}
*{box-sizing:border-box;margin:0;padding:0}
html,body{width:1200px;height:3686px;overflow:hidden}
body{background:var(--cream);font-family:"Poppins",sans-serif;color:var(--ink);position:relative}
.abs{position:absolute}
.heading{font-family:"Jost",sans-serif;font-weight:300;color:var(--teal);letter-spacing:1px;text-transform:uppercase}
.brand{font-family:"Jost",sans-serif;font-weight:400;color:var(--teal);font-size:25px;letter-spacing:1px}
.nav{display:flex;gap:0;font-size:15px;color:var(--ink)}
.nav a{color:inherit;text-decoration:none;position:absolute;white-space:nowrap}
.nav a.active{color:var(--teal)}
.social{display:flex;gap:10px}
.social span{width:34px;height:34px;border-radius:50%;background:var(--white);box-shadow:0 1px 4px rgba(0,0,0,.12);display:block}
.social span:first-child{background:var(--teal)}
.btn{display:inline-flex;align-items:center;justify-content:center;border-radius:22px;font-size:13px;text-transform:uppercase;text-decoration:none}

/* hero */
.hero-photo{left:0;top:0;width:1200px;height:790px;background:linear-gradient(180deg,#f3f2f0 0%,#ecebe8 55%,#f0ebe3 85%,var(--cream) 100%)}
.hero-card{left:600px;top:257px;width:487px;height:315px;background:rgba(255,255,255,.82);padding:38px 46px}
.hero-card h1{font-size:38px;line-height:47px;margin-bottom:20px}
.hero-card p{font-size:15.5px;line-height:26px;color:var(--ink)}

/* services */
.services-title{left:0;width:1200px;top:862px;text-align:center;font-size:45px}
.card{top:957px;width:301px;height:436px;background:var(--white);border-radius:10px;box-shadow:0 4px 18px rgba(0,0,0,.05);text-align:center;padding-top:28px}
.card .icon{width:87px;height:87px;border-radius:50%;background:linear-gradient(135deg,var(--teal),var(--teal-light));margin:0 auto 22px;display:flex;align-items:center;justify-content:center}
.card h3{font-weight:400;font-size:17.5px;margin-bottom:10px}
.card p{font-size:13.5px;line-height:24.7px;color:var(--muted);padding:0 18px}
.card .btn{position:absolute;left:50%;transform:translateX(-50%);top:366px;width:123px;height:42px;background:var(--pale);color:var(--teal)}

/* book */
.book-band{left:0;top:1526px;width:1200px;height:494px;background:linear-gradient(120deg,var(--teal-dark) 0%,#7fb3aa 55%,var(--teal-light) 100%)}
.book-ring{left:113px;top:1573px;width:400px;height:400px;border-radius:50%;background:rgba(255,255,255,.22)}
.book-ring.inner{left:150px;top:1610px;width:326px;height:326px;background:rgba(255,255,255,.28)}
.book-cover{left:205px;top:1613px;width:214px;height:321px;background:linear-gradient(180deg,#efe9e0,#d9cfc2 60%,#eee8df);box-shadow:0 3px 10px rgba(0,0,0,.15)}
.book-title{left:597px;top:1630px;font-size:45px;color:var(--white)}
.book-text{left:600px;top:1700px;width:490px;font-size:15px;line-height:26.5px;color:var(--white)}
.book-btn{left:600px;top:1863px;width:115px;height:42px;background:var(--white);color:var(--ink)}

/* about */
.meet-title{left:108px;top:2178px;font-size:45px}
.meet-text{left:112px;top:2250px;width:489px;font-size:14.8px;line-height:25px;color:var(--ink);text-align:justify}
.meet-text p{margin-bottom:10px}
.meet-btn{left:112px;top:2541px;width:131px;height:43px;background:var(--teal);color:var(--white)}
.meet-photo{left:682px;top:2127px;width:409px;height:519px;border:7px solid var(--white);border-radius:14px;background:linear-gradient(160deg,#d8d2ca,#b9b2a8 45%,#c9c3bb 70%,#a99e92);box-shadow:0 2px 10px rgba(0,0,0,.06)}

/* message */
.message-title{left:0;width:1200px;top:2740px;text-align:center;font-size:45px}
.message-text{left:120px;top:2820px;width:960px;text-align:center;font-size:14.5px;line-height:25px;color:var(--ink)}
.message-text p{margin-bottom:13px}

/* newsletter */
.news-band{left:0;top:3125px;width:1200px;height:308px;background:linear-gradient(120deg,var(--teal-dark),#86b8af 60%,var(--teal-light))}
.news-title{left:0;width:1200px;top:3190px;text-align:center;font-size:44px;line-height:50px;color:var(--white)}
.news-input{left:184px;top:3317px;width:710px;height:42px;border-radius:22px;background:rgba(255,255,255,.25);color:var(--white);font-size:14px;padding-left:22px;display:flex;align-items:center}
.news-btn{left:901px;top:3317px;width:116px;height:42px;background:var(--white);color:var(--ink)}

/* footer */
.footer-rule{left:112px;top:3628px;width:977px;height:1px;background:#cfc9bf}
.copyright{left:0;width:1200px;top:3642px;text-align:center;font-size:13px;color:var(--ink)}
</style>
</head>
<body>

<!-- header -->
<div class="hero-photo abs" role="img" aria-label="Smiling educator seated at a bright white desk with a laptop, glasses and a plant"></div>
<div class="brand abs" style="left:112px;top:48px">PraisewithPellar</div>
<nav class="nav abs" style="left:0;top:53px;width:1200px">
  <a class="active" style="left:517px">Home</a>
  <a style="left:599px">About Me</a>
  <a style="left:709px">Shop</a>
  <a style="left:785px">Book</a>
  <a style="left:858px">Contact</a>
</nav>
<div class="social abs" style="left:965px;top:48px" aria-label="Social links"><span></span><span></span><span></span></div>

<section class="hero-card abs">
  <h1 class="heading">Your school<br>can absolutely<br>thrive.</h1>
  <p>Let's partner together to revolutionize your school's culture Into an engaged, high-performing community where everyone belongs. (Why wait?)</p>
</section>

<!-- services -->
<h2 class="services-title heading abs">What we do</h2>

<article class="card abs" style="left:112px">
  <div class="icon"><svg width="44" height="44" viewBox="0 0 44 44" fill="none" stroke="#fff" stroke-width="2.4"><circle cx="22" cy="22" r="8"/><path d="M22 6v6M22 32v6M6 22h6M32 22h6M11 11l4 4M29 29l4 4M33 11l-4 4M15 29l-4 4"/></svg></div>
  <h3>Digital Tools</h3>
  <p>From staff and student events, to ___ these digital tools are just one File. Print. away from revolutionizing your school culture. (Printed in color of course) (Get that color ink ready!)</p>
  <a class="btn">Shop Now</a>
</article>
<article class="card abs" style="left:449px">
  <div class="icon"><svg width="44" height="44" viewBox="0 0 44 44" fill="none" stroke="#fff" stroke-width="2.4"><path d="M15 28a11 11 0 1 1 14 0v5H15z"/><path d="M17 38h10"/><circle cx="22" cy="19" r="4"/></svg></div>
  <h3>Innovatice Courses</h3>
  <p>Join an individual or team online training course designed to elevate your leadership skills, revolutionize your school culture or transform student behvaior. (And you can even say you thought of it yourself) IDK something at the end</p>
  <a class="btn">Learn More</a>
</article>
<article class="card abs" style="left:787px">
  <div class="icon"><svg width="44" height="44" viewBox="0 0 44 44" fill="none" stroke="#fff" stroke-width="2.4" stroke-linejoin="round"><path d="M4 24l8-8 6 3 6-4 6 2 10 7-10 9-5-4-6 5-6-4z"/><circle cx="30" cy="10" r="5"/><path d="M28 10l2 2 3-4"/></svg></div>
  <h3>Authentic Coaching</h3>
  <p>Unleash your leadership potential in this mentorship experience as we work together to curate a personalized plan to (Let's Be Smart Friends!)</p>
  <a class="btn">Partner</a>
</article>

<!-- book -->
<div class="book-band abs"></div>
<div class="book-ring abs"></div>
<div class="book-ring inner abs"></div>
<div class="book-cover abs" role="img" aria-label="Cover of the book Start With Culture by Pellar Hastings"></div>
<h2 class="book-title heading abs" style="color:var(--white)">Purchase Book</h2>
<p class="book-text abs">The most important tool to connect your community and create a high-performing, thriving culture is YOU! Start by unleashing a people-centered leadership style and learn all the #1 Rules to create the culture you dream about by reading an Readwell #1 New Release Start With Culture.</p>
<a class="btn book-btn abs">Buy Now</a>

<!-- about -->
<h2 class="meet-title heading abs">Meet me</h2>
<div class="meet-text abs">
  <p>(Why, hello there!) Welcome to PraisewithPellar! I am Pellar Hastings an Elementary Principal in Brookvale, Ohio, Author of Start With Culture, and Education Consultant. I am super passionate about bringing change to the way school leaders serve –both children and adults.</p>
  <p>I was a teacher for eight years, and then an instructional coach, before earning my dream job as an elementary school principal! I am now in my sixth year as a school leader and have dramatically shifted the traditional elementary school culture into a thriving, loving community.</p>
</div>
<a class="btn meet-btn abs">Contact Me</a>
<div class="meet-photo abs" role="img" aria-label="Two colleagues smiling while working together at a laptop"></div>

<!-- message -->
<h2 class="message-title heading abs">A message from me</h2>
<div class="message-text abs">
  <p>I am so happy you are here! (Seriously!) Working with other educational leaders brings me THE. MOST. JOY. (I'm OBSESSED)</p>
  <p>I want to support you on every inch of your journey! We can work alongside each other to navigate the challenges of leading adults, transforming student behaviors, and creating a vibrant atmosphere.</p>
  <p>School leadership can be lonely, taxing, and overwhelming. Often, the biggest challenge is knowing where to start as you face the pressures and demands from the many stakeholders. But don't worry, I can't wait to help you!</p>
  <p>So whether you need tools to enhance your own leadership skills, to facilitate connection within your community, or to transform student behaviors, I am here to help you develop your school into a high-performing culture. Let's get started today!!</p>
</div>

<!-- newsletter -->
<div class="news-band abs"></div>
<h2 class="news-title heading abs" style="color:var(--white)">Sign-up for the<br>PraisewithPellar newsletter</h2>
<div class="news-input abs">Email Address</div>
<a class="btn news-btn abs">Sign Up</a>

<!-- footer -->
<div class="brand abs" style="left:112px;top:3535px;font-size:28px">PraisewithPellar</div>
<nav class="nav abs" style="left:0;top:3518px;width:1200px;font-size:17px">
  <a style="left:528px">Home</a><a style="left:608px">|</a>
  <a style="left:647px">About Me</a><a style="left:760px">|</a>
  <a style="left:797px">Shop</a><a style="left:872px">|</a>
  <a style="left:908px">Book</a><a style="left:982px">|</a>
  <a style="left:1018px">Contact</a>
</nav>
<div class="social abs" style="left:965px;top:3555px" aria-label="Social links"><span></span><span></span><span></span></div>
<div class="footer-rule abs"></div>
<p class="copyright abs">© 2024 PRAISEWITHPELLAR &nbsp;| &nbsp; All Rights Reserved</p>

</body>
</html>
```